Stationery for a private security company, "Brennock Security Services Ltd."

Needed is a stationery design for a private security company. The designs must show professionalism and that our company mean nothing but business. Watermark of the company logo on the letterhead page is also a must. The final design must represent innovation and professionalism. It would be great if designers could integrate the colours black and silver onto the cards and letterheads..

Thank you

```html
<!DOCTYPE html>
<html lang="en">
<head>
<meta charset="utf-8">
<title>Brennock Security Services Ltd. — Stationery</title>
<link rel="stylesheet" href="https://fonts.googleapis.com/css2?family=Montserrat:wght@400;600&display=swap">
<style>
  :root {
    --backdrop: #e9e9e9;
    --paper: #ffffff;
    --ink: #1c1c1c;
    --ink-soft: #4a4a4a;
    --silver-faint: #e4e4e4;
    --shadow: 0 6px 18px rgba(0,0,0,0.12);
  }
  * { box-sizing: border-box; margin: 0; padding: 0; }
  html, body { width: 1200px; height: 1000px; overflow: hidden; }
  body {
    background: var(--backdrop);
    font-family: "Montserrat", Arial, sans-serif;
    color: var(--ink);
    position: relative;
  }
  .sheet {
    position: absolute;
    background: var(--paper);
    box-shadow: var(--shadow);
    overflow: hidden;
  }
  .brand {
    position: relative;
    z-index: 1;
    display: flex;
    align-items: center;
    gap: 8px;
    font-weight: 600;
    color: var(--ink);
    letter-spacing: 0.04em;
    text-transform: uppercase;
    line-height: 1.15;
  }
  .brand-dot { flex: none; border-radius: 50%; background: var(--ink); }
  .watermark {
    position: absolute;
    border-radius: 50%;
    border: 28px solid var(--silver-faint);
  }

  /* Business cards */
  .card { width: 260px; height: 160px; top: 130px; }
  .card-back { left: 60px; display: flex; align-items: flex-start; justify-content: flex-start; padding: 58px 0 0 30px; }
  .card-back .brand { font-size: 13px; }
  .card-back .brand-dot { width: 12px; height: 12px; }
  .card-back .watermark { width: 150px; height: 150px; right: -70px; bottom: -90px; border-width: 22px; }

  .card-front { left: 340px; padding: 14px 20px; font-size: 7.5px; color: var(--ink-soft); }
  .card-front .brand { font-size: 8.5px; position: absolute; top: 14px; right: 18px; }
  .card-front .brand-dot { width: 7px; height: 7px; }
  .card-front .details { position: relative; z-index: 1; }
  .card-front .web { margin-top: 24px; }
  .card-front .person { margin-top: 8px; font-weight: 600; font-size: 9px; color: var(--ink); letter-spacing: 0.06em; }
  .card-front .role { font-size: 7px; margin-bottom: 6px; }
  .card-front p { line-height: 1.45; letter-spacing: 0.03em; }
  .card-front .watermark { width: 110px; height: 110px; right: -45px; bottom: -55px; border-width: 18px; }

  /* Envelope */
  .envelope { left: 60px; top: 480px; width: 540px; height: 272px; }
  .envelope .brand { position: absolute; top: 26px; right: 30px; font-size: 15px; }
  .envelope .brand-dot { width: 14px; height: 14px; }
  .envelope .watermark { width: 300px; height: 300px; left: -110px; bottom: -160px; border-width: 40px; }

  /* Letterhead */
  .letterhead { left: 640px; top: 130px; width: 500px; height: 707px; }
  .letterhead .brand { position: absolute; top: 34px; right: 40px; font-size: 14px; }
  .letterhead .brand-dot { width: 13px; height: 13px; }
  .letterhead .watermark { width: 340px; height: 340px; right: -150px; bottom: 90px; border-width: 44px; }
  .letterhead .footer {
    position: absolute; left: 40px; bottom: 32px; z-index: 1;
    font-size: 8px; color: var(--ink-soft); letter-spacing: 0.05em; line-height: 1.7;
    text-transform: uppercase;
  }
</style>
</head>
<body>

  <section class="sheet card card-back" aria-label="Business card, reverse">
    <div class="watermark" aria-hidden="true"></div>
    <div class="brand"><span class="brand-dot"></span><span>Brennock<br>Security Services Ltd.</span></div>
  </section>

  <section class="sheet card card-front" aria-label="Business card, front">
    <div class="watermark" aria-hidden="true"></div>
    <div class="brand"><span class="brand-dot"></span><span>Brennock</span></div>
    <div class="details">
      <p class="web">Web | www.brennocksecurity.co.uk</p>
      <p class="person">MARTIN HALE</p>
      <p class="role">(Director)</p>
      <p>mhale@brennocksecurity.co.uk</p>
      <p>Phone | +44 0800 410 2716</p>
      <p>Fax | +44 0800 410 2719</p>
      <p>Harrier House | 14 Ashgrove Road</p>
      <p>Kelbrook | Hampshire | GU19 4LT</p>
    </div>
  </section>

  <section class="sheet envelope" aria-label="DL envelope">
    <div class="watermark" aria-hidden="true"></div>
    <div class="brand"><span class="brand-dot"></span><span>Brennock<br>Security Services Ltd.</span></div>
  </section>

  <section class="sheet letterhead" aria-label="Letterhead">
    <div class="watermark" aria-hidden="true"></div>
    <div class="brand"><span class="brand-dot"></span><span>Brennock<br>Security Services Ltd.</span></div>
    <div class="footer">
      <p>Harrier House | 14 Ashgrove Road | Kelbrook | Hampshire | GU19 4LT</p>
      <p>Phone | +44 0800 410 2716 | Fax | +44 0800 410 2719</p>
    </div>
  </section>

</body>
</html>
```